Real Estate Sales and Marketing brochures

I have a few templates I uploaded of my old presentations and what I would like to see as a new presentation. I need 1 buyer (7-10 slides), 1 seller (8-12 slides), and 1 about me|us (4-5 slides) presentation. Those 3 would most likely contain 1-2 of the same slides and be 7-10 slides away. I would like it in power point presentation as well as pdf.

I am looking for something very clean, consistent, crisp, bright pictures (of the North Ga area.. Lake Morrow, North Ga Mtns, and the town of Forsyth County along with some really nice homes as the background). I have permission to use this photographers photos (he is my photographer). http://www.corvinstudio.net (go to interiors and exteriors) and http://blog.corvinstudio.net

The goal is to WoW people like my friends presentation labeled RMT does and 1: tell them what they will get with the list their home with us 2: when the buy with us and 3: who we are and what we have accomplished.

If I can get going in the right direction I would like to add stationary, letterhead, etc. to the order. My goal is to have great presentations and then have my flyers and all other printed materials match.

Target Market(s)

Buyers, sellers, and investors in the Real Estate Industry.

Industry/Entity Type

Real Estate Agent

Font styles to use
Serif

Colors
f04a50
85acd3

Requirements
Must have
• 1. about us 2. our services 3. our achievements 4. the process 5. about HB.
• Over 100m in sales (numbers and other awards can be seen at harborwithhale.net). Voted Best of Forsyth County by our Clients, 141,000 total votes, in the Ridgefield Ledger. North Ga's sole Realtor for Home Advisors We Rely On program.
Nice to have
• NICE clean pictures as the background
Should not have
• Dates on any logos or information other than achievements

```html
<!DOCTYPE html>
<html lang="en">
<head>
<meta charset="utf-8">
<title>Your Custom Home Marketing Plan</title>
<link href="https://fonts.googleapis.com/css2?family=EB+Garamond:ital,wght@0,400;1,400&display=swap" rel="stylesheet">
<style>
  :root {
    --page-bg: #e9e9e9;
    --photo-wood: #9a6434;
    --photo-wood-light: #c89a62;
    --photo-wall: #d8b888;
    --photo-sky: #c6d4e0;
    --photo-leaf: #7c9a52;
    --photo-floor: #ecebe8;
    --band-dark: #2e2e30;
    --band-mid: #48484b;
    --band-rule: #707073;
    --title-ink: #f4f4f4;
    --subtitle-ink: #d0d0d0;
  }
  * { margin: 0; padding: 0; box-sizing: border-box; }
  html, body {
    width: 1200px;
    height: 720px;
    overflow: hidden;
    background: var(--page-bg);
  }
  .cover {
    position: relative;
    width: 1200px;
    height: 720px;
    overflow: hidden;
  }
  .cover-photo {
    position: absolute;
    inset: 0;
    background:
      radial-gradient(ellipse 420px 360px at 8% 48%, var(--photo-sky) 0%, rgba(198,212,224,0) 100%),
      radial-gradient(ellipse 360px 380px at 94% 30%, var(--photo-leaf) 0%, rgba(124,154,82,0) 100%),
      radial-gradient(ellipse 700px 300px at 55% 5%, var(--photo-wood) 0%, rgba(154,100,52,0) 100%),
      linear-gradient(180deg, var(--photo-wood-light) 0%, var(--photo-wall) 50%, #e2d6c4 66%, var(--photo-floor) 80%, var(--photo-floor) 100%);
  }
  .title-band {
    position: absolute;
    left: 0;
    top: 455px;
    width: 1200px;
    height: 150px;
    background: linear-gradient(180deg, var(--band-mid) 0%, var(--band-dark) 100%);
    box-shadow: 0 6px 18px rgba(0,0,0,0.18);
  }
  .band-rule {
    position: absolute;
    top: 16px;
    width: 1px;
    height: 118px;
    background: var(--band-rule);
  }
  .band-rule.left { left: 105px; }
  .band-rule.right { right: 105px; }
  .band-text {
    position: absolute;
    left: 130px;
    top: 14px;
    font-family: "EB Garamond", Georgia, serif;
  }
  .cover-title {
    font-size: 66px;
    font-weight: 400;
    color: var(--title-ink);
    line-height: 1.1;
    white-space: nowrap;
  }
  .cover-title em { font-style: italic; }
  .presenter {
    margin-top: 2px;
    margin-left: 44px;
    font-size: 32px;
    color: var(--subtitle-ink);
    white-space: nowrap;
  }
</style>
</head>
<body>
  <main class="cover">
    <div class="cover-photo" role="img" aria-label="Bright interior of a spacious lobby with tall windows, wood-paneled ceiling, pendant globe lights, lounge seating and potted palms"></div>
    <section class="title-band">
      <span class="band-rule left"></span>
      <span class="band-rule right"></span>
      <div class="band-text">
        <h1 class="cover-title"><em>Your</em> Custom Home Marketing Plan</h1>
        <p class="presenter">Presented by: Ryan Hale</p>
      </div>
    </section>
  </main>
</body>
</html>
```